Thermostat Screen Design

We need a screen layout design for a new thermostat we're currently developing. If you're not familiar with thermostats, you can see some examples here - http://smart-climate-units-guide.bestpickdigest.com/

We're after the main page design, with icons, colours etc. It needs to be clean, modern and minimalistic. Attached is all components required on the screen. The screen size is 5 inch (diagnol).

The arrows on the screen showcase what happens when you press a button. For example, when you press MODE once you get OFF, press it twice, HEAT, press it 3 times, COOL, etc. This is just for your reference.

You have complete creative license on how you choose to layout the screen, position the components etc, but we require:

- it must be on a 5 inch screen diagnol
- modern, clean and minimalistic
- includes icons and colours
- Intuitive

Let me know if any questions.

```html
<!DOCTYPE html>
<html lang="en">
<head>
<meta charset="utf-8">
<title>Thermostat Main Screen</title>
<link rel="stylesheet" href="https://fonts.googleapis.com/css2?family=Encode+Sans:wght@200;300;400&display=swap">
<style>
  :root{
    --screen-bg:#235a80;
    --info-bar:#1d4a6c;
    --panel:#1f4f74;
    --sidebar:#2197a3;
    --sidebar-active:#1b8693;
    --sidebar-line:#4cb3bd;
    --accent:#2aa5ae;
    --text:#ffffff;
    --text-soft:#d5e4ee;
    --text-muted:#6f95b3;
    --divider:#4e7da0;
    --button-border:#3c78a0;
  }
  *{box-sizing:border-box;margin:0;padding:0}
  html,body{width:1200px;height:680px;overflow:hidden;background:var(--screen-bg)}
  body{font-family:"Encode Sans",sans-serif;color:var(--text);position:relative}

  .sidebar{position:absolute;left:0;top:0;width:156px;height:680px;background:var(--sidebar)}
  .nav-item{position:absolute;left:0;width:156px;display:flex;flex-direction:column;align-items:center;border-bottom:2px solid var(--sidebar-line);font-size:27px;font-weight:300}
  .nav-item svg{margin-bottom:10px}
  .nav-item.is-active{background:var(--sidebar-active)}
  .nav-mode{top:0;height:168px;padding-top:40px}
  .nav-fan{top:168px;height:172px;padding-top:40px}
  .nav-settings{top:340px;height:174px;padding-top:42px}
  .nav-zones{top:514px;height:166px;padding-top:44px;border-bottom:none}

  .status-bar{position:absolute;top:0;left:156px;right:0;height:91px;font-size:26px;font-weight:300;color:var(--text-soft);letter-spacing:.5px}
  .status-item{position:absolute;top:24px}
  .status-sep{position:absolute;top:28px;width:1px;height:24px;background:var(--divider)}
  .clock{position:absolute;left:767px;top:6px;font-size:53px;font-weight:300;color:var(--text);letter-spacing:.5px}

  .info-bar{position:absolute;left:200px;top:91px;width:952px;height:97px;background:var(--info-bar)}
  .info-divider{position:absolute;left:479px;top:0;width:2px;height:97px;background:var(--panel)}
  .reading{position:absolute;top:18px;display:flex;align-items:center}
  .reading-label{font-size:25px;font-weight:300;color:var(--text-soft);margin-right:14px}
  .reading-value{font-size:50px;font-weight:300}
  .reading-value sup{font-size:22px;vertical-align:26px}
  .reading svg{margin-left:14px}

  .main-panel{position:absolute;left:200px;top:188px;width:952px;height:402px;background:var(--panel)}
  .room-temp{position:absolute;left:68px;top:-8px;font-size:318px;font-weight:200;line-height:1;letter-spacing:-6px}
  .room-temp-degree{position:absolute;left:398px;top:56px;font-size:42px;font-weight:200}
  .room-temp-label{position:absolute;left:78px;top:324px;font-size:27px;font-weight:300;letter-spacing:3px;color:var(--text-muted)}

  .setpoint{position:absolute;left:516px;display:flex;align-items:center}
  .setpoint-label{width:208px;font-size:26px;font-weight:300;color:var(--text-soft)}
  .setpoint-value{width:112px;font-size:50px;font-weight:300}
  .setpoint-cool{top:120px}
  .setpoint-heat{top:206px}
  .step-button{width:54px;height:54px;border-radius:6px;background:var(--accent);display:flex;align-items:center;justify-content:center}

  .action-button{position:absolute;top:604px;width:223px;height:68px;border:2px solid var(--button-border);border-radius:8px;display:flex;align-items:center;justify-content:center;font-size:27px;font-weight:300}
  .action-button svg{margin-right:14px}
</style>
</head>
<body>

<nav class="sidebar">
  <div class="nav-item nav-mode">
    <svg width="60" height="54" viewBox="0 0 60 54" fill="none" stroke="#fff" stroke-width="4" stroke-linecap="round">
      <g transform="translate(22 22)">
        <line x1="0" y1="-18" x2="0" y2="18"/><line x1="-15.6" y1="-9" x2="15.6" y2="9"/><line x1="-15.6" y1="9" x2="15.6" y2="-9"/>
        <polyline points="-5,-14 0,-9 5,-14"/><polyline points="-5,14 0,9 5,14"/>
      </g>
      <path d="M46 28c6 6 8 10 8 15a10 10 0 0 1-20 0c0-4 3-6 4-10 2 3 3 4 5 4-1-4 0-6 3-9z" fill="#fff" stroke="none"/>
    </svg>
    Mode
  </div>
  <div class="nav-item nav-fan is-active">
    <svg width="64" height="64" viewBox="-32 -32 64 64" fill="#fff">
      <circle r="7"/>
      <path d="M-4-8C-12-14-10-28 2-29 14-29 16-16 6-9z"/>
      <path d="M-4-8C-12-14-10-28 2-29 14-29 16-16 6-9z" transform="rotate(120)"/>
      <path d="M-4-8C-12-14-10-28 2-29 14-29 16-16 6-9z" transform="rotate(240)"/>
      <circle r="4" fill="#1b8693"/>
    </svg>
    Fan
  </div>
  <div class="nav-item nav-settings">
    <svg width="50" height="56" viewBox="0 0 50 56" fill="#fff">
      <rect x="6" y="2" width="4" height="52"/><rect x="23" y="2" width="4" height="52"/><rect x="40" y="2" width="4" height="52"/>
      <rect x="2" y="34" width="12" height="8"/><rect x="19" y="12" width="12" height="8"/><rect x="36" y="26" width="12" height="8"/>
    </svg>
    Settings
  </div>
  <div class="nav-item nav-zones">
    <svg width="60" height="40" viewBox="0 0 60 40" fill="none" stroke="#fff" stroke-width="3.5" stroke-linecap="round">
      <path d="M16 8a18 18 0 0 0 0 24"/><path d="M44 8a18 18 0 0 1 0 24"/>
      <path d="M8 2a28 28 0 0 0 0 36"/><path d="M52 2a28 28 0 0 1 0 36"/>
      <circle cx="30" cy="20" r="2" fill="#fff" stroke="none"/>
    </svg>
    Zones
  </div>
</nav>

<header class="status-bar">
  <span class="status-item" style="left:53px">SLEEP</span>
  <span class="status-sep" style="left:187px"></span>
  <span class="status-item" style="left:241px">ZONE 1</span>
  <span class="status-sep" style="left:380px"></span>
  <svg class="status-item" style="left:430px;top:26px" width="26" height="26" viewBox="0 0 26 26" fill="var(--text-muted)">
    <rect x="1" y="4" width="24" height="21" rx="2"/><rect x="5" y="0" width="3" height="6"/><rect x="18" y="0" width="3" height="6"/>
    <g fill="var(--screen-bg)"><rect x="4" y="10" width="4" height="3"/><rect x="11" y="10" width="4" height="3"/><rect x="18" y="10" width="4" height="3"/><rect x="4" y="16" width="4" height="3"/><rect x="11" y="16" width="4" height="3"/><rect x="18" y="16" width="4" height="3"/></g>
  </svg>
  <span class="status-item" style="left:474px">MON 7-10-2014</span>
  <span class="status-sep" style="left:721px"></span>
  <span class="clock">09:28 AM</span>
</header>

<section class="info-bar">
  <div class="reading" style="left:84px">
    <span class="reading-label">Outdoor Temp:</span>
    <span class="reading-value">28<sup>o</sup></span>
    <svg width="62" height="62" viewBox="-31 -31 62 62" fill="none" stroke="var(--text-soft)" stroke-width="2.5" stroke-linecap="round">
      <circle r="12"/>
      <g><line y1="-18" y2="-26"/><line y1="18" y2="26"/><line x1="-18" x2="-26"/><line x1="18" x2="26"/>
      <line x1="-13" y1="-13" x2="-18" y2="-18"/><line x1="13" y1="13" x2="18" y2="18"/><line x1="-13" y1="13" x2="-18" y2="18"/><line x1="13" y1="-13" x2="18" y2="-18"/></g>
    </svg>
  </div>
  <div class="info-divider"></div>
  <div class="reading" style="left:579px">
    <span class="reading-label">Indoor RH:</span>
    <span class="reading-value">25<sup>o</sup></span>
    <svg width="52" height="52" viewBox="0 0 52 52" fill="none" stroke="var(--text-soft)" stroke-width="2.5" stroke-linejoin="round">
      <path d="M4 24L26 5l22 19"/><path d="M10 20v26h32V20"/><path d="M21 46V32h10v14"/>
    </svg>
  </div>
</section>

<main class="main-panel">
  <div class="room-temp">26</div>
  <div class="room-temp-degree">O</div>
  <div class="room-temp-label">ROOM TEMPERATURE</div>

  <div class="setpoint setpoint-cool">
    <span class="setpoint-label">Cool Setpoint :</span>
    <span class="setpoint-value">55</span>
    <span class="step-button" aria-label="Raise setpoint"><svg width="22" height="14" viewBox="0 0 22 14"><path d="M11 0L22 14H0z" fill="#fff"/></svg></span>
  </div>
  <div class="setpoint setpoint-heat">
    <span class="setpoint-label">Heat Setpoint:</span>
    <span class="setpoint-value">25</span>
    <span class="step-button" aria-label="Lower setpoint"><svg width="22" height="14" viewBox="0 0 22 14"><path d="M0 0H22L11 14z" fill="#fff"/></svg></span>
  </div>
</main>

<div class="action-button" style="left:204px">Heat</div>
<div class="action-button" style="left:444px">
  <svg width="40" height="40" viewBox="-20 -20 40 40" fill="none" stroke="var(--text-soft)" stroke-width="2.2">
    <circle r="4"/>
    <path d="M-3-5C-8-9-7-18 1-18 9-18 10-10 4-6z"/>
    <path d="M-3-5C-8-9-7-18 1-18 9-18 10-10 4-6z" transform="rotate(120)"/>
    <path d="M-3-5C-8-9-7-18 1-18 9-18 10-10 4-6z" transform="rotate(240)"/>
  </svg>
  Auto
</div>
<div class="action-button" style="left:685px" aria-label="Cool">
  <svg width="44" height="44" viewBox="-22 -22 44 44" fill="none" stroke="var(--text-soft)" stroke-width="3" stroke-linecap="round" style="margin:0">
    <line y1="-19" y2="19"/><line x1="-16.5" y1="-9.5" x2="16.5" y2="9.5"/><line x1="-16.5" y1="9.5" x2="16.5" y2="-9.5"/>
    <polyline points="-5,-15 0,-10 5,-15"/><polyline points="-5,15 0,10 5,15"/>
    <polyline points="-15,-3 -9,-5 -11,-11" /><polyline points="15,3 9,5 11,11"/>
    <polyline points="-15,3 -9,5 -11,11"/><polyline points="15,-3 9,-5 11,-11"/>
  </svg>
</div>
<div class="action-button" style="left:925px">Zone 1</div>

</body>
</html>
```